Business Card for IT Support Company
Aide Nova
Business Card for IT Support Company - Information Technology
Creative Brief
Professional
Assistance Informatique 24/7
Tél. 0900 417 536
2.50 CHF/min de 8h à 22h et 3.50 CHF/min de 22h à 8h depuis le réseau fixe.
info@aide-nova.ch
http://www.aide-nova.ch
No specific name, this is only a hotline IT support number Business Card (phone number is in the title) in Address box, it's the rates on the Business Number. We will use brivopress . ch as the printing company, here are the exact size in mm they send to me: Business card Size is 85x55mm (But file dimension must be 91x61mm) Colors needs to be send in CMYK, minimum 200 dpi, maximum quality.
- Contrôle à distance PC/MAC - Support technique informatique - Formation / Consulting / Coaching - Infographie / Graphisme - Création de Site Web - Smartphone / Tablette

```html
<!DOCTYPE html>
<html lang="fr">
<head>
<meta charset="utf-8">
<title>Aide Nova – Business Card</title>
<link rel="stylesheet" href="https://fonts.googleapis.com/css2?family=Arimo:wght@400;700&display=swap">
<style>
  :root {
    --page-bg: #e6e4e1;
    --card-white: #ffffff;
    --card-silver: #e9e9ea;
    --ink-black: #111111;
    --ink-dark: #2a2a2a;
    --ink-grey: #6b6b6b;
    --brand-red: #e0141e;
    --brand-red-dark: #a40d14;
    --text-light: #f4f4f4;
  }
  * { box-sizing: border-box; margin: 0; padding: 0; }
  html, body {
    width: 1200px; height: 901px; overflow: hidden;
    background: var(--page-bg);
    font-family: "Arimo", Arial, sans-serif;
  }
  .cards {
    position: absolute; inset: 0;
    display: flex; align-items: center; justify-content: center; gap: 60px;
  }
  .card {
    position: relative;
    width: 520px; height: 336px;
    border-radius: 26px;
    overflow: hidden;
    box-shadow: 0 10px 28px rgba(0,0,0,.18);
  }
  .card-front { background: linear-gradient(180deg, var(--card-white) 0%, var(--card-silver) 100%); }

  .front-band {
    position: absolute; left: 0; right: 0; top: 172px; bottom: 0;
    background: linear-gradient(180deg, var(--brand-red) 0%, var(--brand-red-dark) 14%, var(--ink-black) 30%, var(--ink-black) 100%);
  }

  .brand {
    position: absolute; left: 34px; top: 94px;
    display: flex; align-items: center; gap: 12px;
  }
  .brand-dot {
    width: 34px; height: 34px; border-radius: 50%;
    background: var(--brand-red);
    flex: none;
  }
  .brand-name {
    font-size: 28px; font-weight: 700; color: var(--ink-dark); letter-spacing: .5px;
    white-space: nowrap;
  }
  .hotline {
    position: absolute; right: 34px; top: 92px; text-align: right;
  }
  .hotline-label {
    font-size: 13px; font-weight: 700; color: var(--brand-red); letter-spacing: 1px;
  }
  .hotline-number {
    font-size: 26px; font-weight: 700; color: var(--ink-black); letter-spacing: 1.5px;
    white-space: nowrap;
  }
  .contact {
    position: absolute; left: 190px; top: 236px;
    color: var(--text-light); font-size: 16px; letter-spacing: 1.5px;
    text-transform: uppercase; line-height: 1.9;
  }

  .card-back {
    background: var(--card-white);
    display: flex; flex-direction: column; justify-content: center;
    padding: 0 44px;
  }
  .services { list-style: none; }
  .service {
    font-size: 14px; color: var(--ink-grey); line-height: 2.1;
  }
  .service::before { content: "– "; color: var(--brand-red); }
</style>
</head>
<body>
<main class="cards">
  <section class="card card-front" aria-label="Card front">
    <div class="front-band" role="img" aria-label="Red and black decorative wave band"></div>
    <div class="brand">
      <span class="brand-dot"></span>
      <span class="brand-name">Aide Nova 24/7</span>
    </div>
    <div class="hotline">
      <p class="hotline-label">CALL US TODAY</p>
      <p class="hotline-number">0900 417 536</p>
    </div>
    <div class="contact">
      <p>info@aide-nova.ch</p>
      <p>www.aide-nova.ch</p>
    </div>
  </section>

  <section class="card card-back" aria-label="Card back">
    <ul class="services">
      <li class="service">Contrôle à distance PC/MAC / Support technique informatique</li>
      <li class="service">Formation / Consulting / Coaching</li>
      <li class="service">Infographie / Graphisme</li>
      <li class="service">Création de Site Web</li>
      <li class="service">Smartphone / Tablette</li>
    </ul>
  </section>
</main>
</body>
</html>
```